Checkout sign

Wall sign for clinic checkout.
“The Good Lord does ALL the healing..
But we DO collect the co-pay”

Add Celtic cross at top and our logo on bottom

```html
<!DOCTYPE html>
<html lang="en">
<head>
<meta charset="UTF-8">
<title>Checkout Sign</title>
<link href="https://fonts.googleapis.com/css2?family=Noto+Serif:wght@700&display=swap" rel="stylesheet">
<style>
  :root {
    --ink: #2f2a8f;
    --ink-soft: #5a55b5;
    --ink-pale: #8c88d0;
    --paper: #ffffff;
    --backdrop: #ffffff;
  }
  * { margin: 0; padding: 0; box-sizing: border-box; }
  html, body {
    width: 831px;
    height: 1200px;
    overflow: hidden;
    background: var(--backdrop);
  }
  .sign {
    position: relative;
    width: 831px;
    height: 1200px;
    background: var(--paper);
    font-family: "Noto Serif", Georgia, serif;
    color: var(--ink);
  }
  .cross-art {
    position: absolute;
    left: 345px;
    top: 90px;
    width: 141px;
    height: 250px;
    border-radius: 8px;
    background: linear-gradient(180deg, var(--ink-soft), var(--ink));
    opacity: 0.85;
  }
  .message {
    position: absolute;
    left: 0;
    top: 400px;
    width: 100%;
    text-align: center;
    font-weight: 700;
    font-size: 60px;
    line-height: 1.3;
    letter-spacing: 0.5px;
  }
  .clinic-mark {
    position: absolute;
    left: 0;
    top: 880px;
    width: 100%;
    display: flex;
    flex-direction: column;
    align-items: center;
  }
  .clinic-mark svg { display: block; }
  .clinic-name {
    margin-top: 14px;
    font-weight: 700;
    font-size: 40px;
    color: var(--ink);
    text-align: center;
    line-height: 1.1;
  }
  .clinic-name small {
    display: block;
    font-size: 15px;
    letter-spacing: 3px;
    margin-top: 4px;
  }
</style>
</head>
<body>
  <main class="sign">
    <div class="cross-art" role="img" aria-label="Celtic cross with knotwork ring"></div>

    <p class="message">
      The Good Lord does<br>
      ALL the healing..<br>
      But we DO collect<br>
      the co-pay
    </p>

    <div class="clinic-mark">
      <svg width="130" height="130" viewBox="0 0 130 130" aria-hidden="true">
        <circle cx="65" cy="65" r="60" fill="none" stroke="var(--ink)" stroke-width="6"/>
      </svg>
      <div class="clinic-name">
        Brennan
        <small>ORTHOPEDIC CLINIC</small>
      </div>
    </div>
  </main>
</body>
</html>
```